Label design for Japanese healthy drink

We need new label design to give our product a new look. This is Amazake, traditional Japanese drink made out of fermented rice. This is nutrition packed drink and target audience is health conscious people. We want something simple and healthy. The attached photo is current label (for the size reference only) and food pouch the label will be attached. Please don't use anything on the label in the picture.

Target Market(s)

health conscious people (30s - 50s)

Requirements
Must have
• "Amazake"
Should not have
• too much color, picture of rice or sake

```html
<!DOCTYPE html>
<html lang="en">
<head>
<meta charset="UTF-8">
<title>Amazake Label</title>
<link rel="stylesheet" href="https://fonts.googleapis.com/css2?family=Montserrat:wght@400;500;600;700&family=Noto+Sans+JP:wght@700&family=Roboto+Condensed:wght@400&display=swap">
<style>
  :root {
    --backdrop-top: #7a8898;
    --backdrop-bottom: #5e6f80;
    --label-aqua: #68d9dd;
    --cream: #fbf6e2;
    --organic-green: #2ecb8e;
  }
  html, body {
    margin: 0;
    padding: 0;
    width: 1200px;
    height: 849px;
    overflow: hidden;
  }
  body {
    position: relative;
    background: linear-gradient(225deg, var(--backdrop-top) 0%, var(--backdrop-bottom) 60%, var(--backdrop-bottom) 100%);
    font-family: "Montserrat", sans-serif;
  }
  .label {
    position: absolute;
    left: 300px;
    top: 124px;
    width: 600px;
    height: 600px;
    border-radius: 126px;
    background: var(--label-aqua);
    color: var(--cream);
  }
  .label > * {
    position: absolute;
    left: 0;
    width: 100%;
    margin: 0;
    text-align: center;
    white-space: nowrap;
  }
  .label__kanji {
    top: 120px;
    height: 68px;
    line-height: 68px;
    font-family: "Noto Sans JP", sans-serif;
    font-weight: 700;
    font-size: 56px;
    transform: skewX(-10deg);
  }
  .label__name {
    top: 180px;
    height: 110px;
    line-height: 110px;
    font-weight: 600;
    font-size: 96px;
    letter-spacing: 1px;
  }
  .label__tagline {
    top: 277px;
    height: 26px;
    line-height: 26px;
    font-weight: 600;
    font-size: 20px;
    letter-spacing: 0.8px;
  }
  .label__badge {
    left: 178px;
    top: 333px;
    width: 246px;
    height: 78px;
    line-height: 78px;
    border-radius: 4px;
    background: var(--organic-green);
    font-weight: 600;
    font-size: 28px;
    letter-spacing: 2.5px;
  }
  .label__natural {
    top: 443px;
    height: 40px;
    line-height: 40px;
    font-weight: 400;
    font-size: 31px;
    letter-spacing: 0.5px;
  }
  .label__natural strong { font-weight: 600; }
  .label__claims {
    top: 481px;
    height: 22px;
    line-height: 22px;
    font-family: "Roboto Condensed", sans-serif;
    font-size: 16px;
  }
  .label__origin {
    top: 557px;
    height: 22px;
    line-height: 22px;
    font-weight: 600;
    font-size: 17px;
    letter-spacing: 1.2px;
  }
</style>
</head>
<body>
  <main class="label">
    <p class="label__kanji" lang="ja">甘酒</p>
    <h1 class="label__name">AMAZAKE</h1>
    <p class="label__tagline">Fermented Japanese Rice Drink</p>
    <p class="label__badge">ORGANIC</p>
    <p class="label__natural"><strong>100%</strong> NATURAL</p>
    <p class="label__claims">NO ADDED SUGAR, GLUTEN FREE</p>
    <p class="label__origin">MADE IN JAPAN</p>
  </main>
</body>
</html>
```